NZ First of it's kind solutions directory and marketplace for busy Mums needs a business card design

We need a business card design for our new nationwide business in NZ (long term plans to go global). We provide solutions to the everyday challenges that busy Mums face by connecting them with quality communities and suppliers of carefully selected, relevant products and services. We sell direct via our online marketplace. The final design should communicate our values of inclusivity, quality and smart solutions. Colours should incorporate our logo colour palette of #477077 and #6ba8b2. Our website is at https://www.brightnestly.com

Target Market(s)

busy Mums, Age 28 – 50, female, income over $100K, location main centres NZ primarily but NZ wide. Is likely juggling work or career with a young family. Probably had hobbies which have fallen by the wayside.
-Wants to succeed in her chosen career without compromising on family life
-to successfully juggle her career without feeling like she is compromising her children
- Is time poor, something always has to give and it’s generally her health (she’ll stay up late, get stressed)
- probably ex corporate or professional career. Has discretional income

Industry/Entity Type

Business

Contact Information for Business Card

Lena Hartwell, Founder, BrightNestly.com (Strapline Click; Connect; Done), 48 Kowhai Terrace, Ferndale, Auckland 1071, New Zealand. Mob: 021 437 518 Ph: +64 (0)9 581 4706

Font styles to use
Other font styles liked:
• Raleway, and/or Architects Daughter

Colors
00a990
33b8a4
86cfc6
cfeae6

Requirements
Must have
• the above details, streamline. the logo and colours associated with those logos
Should not have
• foil or metallic colours

```html
<!DOCTYPE html>
<html lang="en">
<head>
<meta charset="utf-8">
<title>BrightNestly business card</title>
<link href="https://fonts.googleapis.com/css2?family=Raleway:wght@400;500;800&display=swap" rel="stylesheet">
<style>
  :root {
    --teal-dark: #477077;
    --teal-light: #6ba8b2;
    --teal-fold: #3a5d63;
    --paper: #ffffff;
    --ink: #1f2b2d;
    --backdrop: #d3e8ef;
  }
  * { margin: 0; padding: 0; box-sizing: border-box; }
  html, body { width: 1200px; height: 900px; overflow: hidden; }
  body {
    background: var(--backdrop);
    font-family: "Raleway", sans-serif;
    position: relative;
  }
  .card {
    position: absolute;
    left: 320px;
    width: 560px;
    height: 320px;
    overflow: hidden;
    box-shadow: 0 6px 18px rgba(40, 70, 80, 0.25);
  }
  .card-front { top: 70px; background: var(--teal-dark); }
  .card-back { top: 490px; background: var(--paper); }

  /* Front */
  .front-brand {
    position: absolute;
    left: 0; right: 0; top: 118px;
    display: flex; align-items: center; justify-content: center; gap: 16px;
  }
  .brand-dot {
    width: 34px; height: 34px; border-radius: 50%;
    background: var(--paper);
  }
  .brand-name {
    font-weight: 800;
    font-size: 58px;
    letter-spacing: -1px;
    color: var(--paper);
  }
  .front-url {
    position: absolute; left: 0; right: 0; top: 262px;
    text-align: center;
    font-size: 13px; color: var(--paper); letter-spacing: 0.3px;
  }

  /* Back */
  .back-art { position: absolute; inset: 0; }
  .back-brand {
    position: absolute; left: 28px; top: 68px;
    display: flex; align-items: center; gap: 10px;
  }
  .back-brand .brand-dot { width: 22px; height: 22px; background: var(--teal-dark); }
  .back-brand .brand-name { font-size: 32px; color: var(--teal-dark); letter-spacing: -0.5px; }

  .person {
    position: absolute; left: 310px; top: 24px; width: 250px;
    text-align: center; color: var(--paper);
  }
  .person-name { font-size: 21px; font-weight: 400; line-height: 1.1; }
  .person-role { font-size: 11px; font-weight: 500; }

  .contact-list {
    position: absolute; left: 36px; top: 196px;
    list-style: none;
  }
  .contact-item {
    display: flex; align-items: center; gap: 14px;
    height: 26px;
    font-size: 15px; font-weight: 500; color: var(--ink);
  }
  .contact-icon {
    width: 22px; height: 22px; background: var(--teal-dark);
    display: flex; align-items: center; justify-content: center;
  }

  .address {
    position: absolute; left: 378px; top: 214px; width: 172px;
    text-align: center; color: var(--paper);
    font-size: 11.5px; line-height: 1.5;
  }
  .address-pin { display: block; margin: 0 auto 8px; }
</style>
</head>
<body>

<section class="card card-front">
  <div class="front-brand">
    <span class="brand-dot"></span>
    <span class="brand-name">BrightNestly</span>
  </div>
  <p class="front-url">BrightNestly.com</p>
</section>

<section class="card card-back">
  <svg class="back-art" width="560" height="320" viewBox="0 0 560 320">
    <polygon points="320,0 560,0 560,320 372,320" fill="var(--teal-dark)"/>
    <polygon points="310,92 342,92 342,118" fill="var(--teal-fold)"/>
    <polygon points="310,20 560,20 560,92 310,92" fill="var(--teal-light)"/>
  </svg>

  <div class="back-brand">
    <span class="brand-dot"></span>
    <span class="brand-name">BrightNestly</span>
  </div>

  <div class="person">
    <p class="person-name">Lena Hartwell</p>
    <p class="person-role">Founder</p>
  </div>

  <ul class="contact-list">
    <li class="contact-item">
      <span class="contact-icon">
        <svg width="14" height="14" viewBox="0 0 24 24"><path fill="#fff" d="M6.6 10.8a15 15 0 0 0 6.6 6.6l2.2-2.2c.3-.3.7-.4 1-.2 1.1.4 2.3.6 3.6.6.6 0 1 .4 1 1V20c0 .6-.4 1-1 1A17 17 0 0 1 3 4c0-.6.4-1 1-1h3.5c.6 0 1 .4 1 1 0 1.3.2 2.5.6 3.6.1.3 0 .7-.2 1z"/></svg>
      </span>021 437 518
    </li>
    <li class="contact-item">
      <span class="contact-icon">
        <svg width="14" height="14" viewBox="0 0 24 24"><rect x="3" y="9" width="18" height="12" rx="2" fill="#fff"/><path d="M2 8c0-3 20-3 20 0v2h-5V8H7v2H2z" fill="#fff"/><circle cx="12" cy="15" r="2.5" fill="var(--teal-dark)"/></svg>
      </span>+64 (0)9 581 4706
    </li>
    <li class="contact-item">
      <span class="contact-icon">
        <svg width="14" height="14" viewBox="0 0 24 24"><rect x="2" y="5" width="20" height="14" fill="none" stroke="#fff" stroke-width="2"/><path d="M2 5l10 8 10-8" fill="none" stroke="#fff" stroke-width="2"/></svg>
      </span>hello@brightnestly.com
    </li>
    <li class="contact-item">
      <span class="contact-icon">
        <svg width="14" height="14" viewBox="0 0 24 24"><circle cx="12" cy="12" r="9" fill="none" stroke="#fff" stroke-width="2"/><path d="M3 12h18M12 3c3 3 3 15 0 18M12 3c-3 3-3 15 0 18" fill="none" stroke="#fff" stroke-width="1.6"/></svg>
      </span>www.BrightNestly.com
    </li>
  </ul>

  <div class="address">
    <svg class="address-pin" width="12" height="16" viewBox="0 0 12 16"><path d="M6 0a6 6 0 0 1 6 6c0 4-6 10-6 10S0 10 0 6a6 6 0 0 1 6-6z" fill="#fff"/><circle cx="6" cy="6" r="2.2" fill="var(--teal-dark)"/></svg>
    <p>48 Kowhai Terrace, Ferndale,<br>Auckland 1071, New Zealand</p>
  </div>
</section>

</body>
</html>
```